Re-design of 4 x 2-sided reports

I need the 4 attached reports (3 are 2-sides of A4; 1 is 7-sides of A4) to be re-designed with a consistent look and feel. Just need 1 or 2 images per report being inserted plus consistent branding and contact details being displayed in the same location on each report with same colour, font and design). Reports are attached.
The reports are used as lead magnets.
That is, visitors to our website can download one of them (7 Steps To Sharpen Your Sales Pitch Before Spring Arrives) by filling in a form with their email address. Then over the next 30 days the other reports are sent to the subscriber via email autoresponders.
Blue Harbour Marketing is a marketing consultancy dealing with companies in the North West of England providing cost-effective and profitable marketing to small and medium-sized businesses that want better and quicker results. The reports need to be professional and corporate looking. Please let me know if you need any further clarification or have any questions. I attach an example report. I don't necessarily want to mirror this report (from the law firm) but it may help to understand what look I'm trying to get. Many thanks, Gordon

Target Market(s)

SMEs based in NW of England
Typically with turnover of £1m to £10m or 10 to 100 employees
Clients often in the construction sector, healthcare, accountants, lawyers and local councils.

Industry/Entity Type

Marketing

Font styles to use
Serif
Sans Serif

Colors
ec1f27

Requirements
Must have
• Consistent branding
• Logo in same place across all four reports
• Contact details in same place across all four reports
• Same font across all four reports
• Same colour across all four reports
• Professional and bold look
Nice to have
• Some strong stock photography
• 1 or 2 images per report
• More images for the 7-page report though
Should not have
• No graphics

```html
<!DOCTYPE html>
<html lang="en">
<head>
<meta charset="utf-8">
<title>Blue Harbour Marketing – Social Media Report</title>
<link href="https://fonts.googleapis.com/css2?family=Open+Sans:wght@400&family=Oswald:wght@500&display=swap" rel="stylesheet">
<style>
  :root {
    --brand-red: #b3151d;
    --band-grey: #8f969c;
    --text-dark: #1f1f1f;
    --text-muted: #555a5e;
    --rule-dark: #2a2a2a;
    --network-blue: #1f7bc1;
    --paper: #ffffff;
  }
  * { margin: 0; padding: 0; box-sizing: border-box; }
  html, body { width: 848px; height: 1200px; overflow: hidden; background: var(--paper); }
  .page {
    position: relative;
    width: 848px;
    height: 1200px;
    background: var(--paper);
    font-family: "Open Sans", Arial, sans-serif;
    color: var(--text-dark);
  }
  .top-band {
    position: absolute; left: 0; top: 0; width: 100%; height: 13px;
    background: var(--band-grey);
  }
  .network-heading {
    position: absolute; left: 59px; top: 76px;
    display: flex; align-items: center; gap: 6px;
  }
  .network-mark {
    width: 44px; height: 44px; border-radius: 4px;
    background: var(--network-blue);
  }
  .section-title {
    font-family: "Oswald", "Arial Narrow", sans-serif;
    font-weight: 500;
    color: var(--brand-red);
    font-size: 28px;
    line-height: 1;
    letter-spacing: -0.2px;
  }
  .network-points {
    position: absolute; left: 160px; top: 148px; width: 640px;
    list-style: none;
    font-size: 15.5px; line-height: 20.4px;
  }
  .network-points li { padding-left: 11px; text-indent: -11px; }
  .network-points li::before { content: "●"; font-size: 11px; margin-right: 1px; position: relative; top: -1px; }
  .summary-title {
    position: absolute; left: 57px; top: 357px; font-size: 30px;
  }
  .summary-body {
    position: absolute; left: 57px; top: 420px; width: 734px;
    font-size: 15.5px; line-height: 21.5px; text-align: justify;
  }
  .summary-body p { margin-bottom: 19.5px; }
  .footer-rule {
    position: absolute; left: 57px; top: 1022px; width: 734px; height: 2px;
    background: var(--rule-dark);
  }
  .footer-brand {
    position: absolute; left: 87px; top: 1035px; width: 91px; height: 131px;
    border: 1px solid #d9d9d9;
    display: flex; flex-direction: column; align-items: center; justify-content: flex-start;
    padding-top: 12px; gap: 8px;
  }
  .brand-square { width: 70px; height: 70px; background: var(--brand-red); }
  .brand-name {
    font-family: "Open Sans", Arial, sans-serif;
    font-size: 10.5px; line-height: 12px; text-align: center;
    color: var(--brand-red);
  }
  .footer-web {
    position: absolute; right: 57px; top: 1139px;
    font-size: 16.5px; color: var(--text-muted);
  }
</style>
</head>
<body>
<div class="page">
  <div class="top-band"></div>

  <div class="network-heading">
    <div class="network-mark"></div>
    <h2 class="section-title">ProLink</h2>
  </div>

  <ul class="network-points">
    <li>15 million users in the UK</li>
    <li>347 million users worldwide</li>
    <li>Free advertising of your services and expertise</li>
    <li>Ability to identify prospects</li>
    <li>Free to post jobs on site if you are hiring</li>
    <li>Is becoming part of the ‘sifting’ or selection process of companies wanting new suppliers</li>
    <li>Status Updates = free advertising</li>
    <li>Q &amp; As = show and ‘advertise’ your expertise</li>
  </ul>

  <h2 class="section-title summary-title">Summary</h2>

  <div class="summary-body">
    <p>Social media is now used by millions of people (including many of your customers) both here in the UK and across the world.</p>
    <p>People use it to connect with other people but also to find products and services that they may need.</p>
    <p>Social media provides all businesses with a free, relatively easy way to promote their business to existing and potential new customers.</p>
    <p>Those that are embracing social media and investing some time and effort into learning how to get the most from social media are really helping to grow their businesses.</p>
    <p>For those businesses that haven’t yet considered social media (for whatever reason) or are not taking full advantage of the benefits of social media, they are definitely missing an opportunity to grow their business and are ‘leaving money on the table’.</p>
    <p>We believe it is, therefore, becoming imperative that virtually all businesses participate, to some degree, in social media.</p>
  </div>

  <div class="footer-rule"></div>
  <div class="footer-brand">
    <div class="brand-square"></div>
    <div class="brand-name">Blue Harbour<br>Marketing</div>
  </div>
  <div class="footer-web">www.blueharbourmarketing.co.uk</div>
</div>
</body>
</html>
```